RESTAURANT 4X6 POSTCARD
MARLOW'S TRATTORIA
Creative Brief
Bright & Fun-filled
5172 BRASWELL POND AVE SPRINGFIELD, VA 22987
BLUEPLATE77@EXAMPLEMAIL.NET
this is a greek and italian pizzeria (no flags needed) but ok to use columns or the leaning tower etc to have a nice design. this postcard will be going to all the neighborhoods in the area to bring more business to our restaurant that has been around for 55 years! we want it to portray all the amazing pics of food we have from pizza/calzones, International Burgers, wraps/subs, gyros, salads, sautees, and even breakfast. the back of the card will have a standard place for postage and address label. off to the left is where there will be room for 3 or 4 coupons. $5 OFF any purchase of $25+, HALF PRICE buy one Lunch Entree & receive 2nd Lunch of equal or lesser value for 1/2 price with purchase of 2 soft drinks, Monday&Tuesday Special $8.99 One Large 16" pizza with one topping. Dine-In or Carry-Out. if room 4th coupon will be $5 OFF 2 Large 16" pizzas with 1 or more toppings, Coupons can not be combined and excludes alcohol. we are located in between Brewnook and Fresh Orchard:-) as for the logo. we usually use have Marlows Trattoria written in Red with black outline

```html
<!DOCTYPE html>
<html lang="en">
<head>
<meta charset="utf-8">
<title>Marlow's Trattoria Postcard</title>
<link href="https://fonts.googleapis.com/css2?family=Anton&family=Oswald:wght@400;600;700&display=swap" rel="stylesheet">
<style>
:root{
  --stage:#9b9b9b;
  --red:#e4161b;
  --red-deep:#b80d10;
  --white:#ffffff;
  --ink:#1b1b1b;
  --yellow:#ffd21f;
  --food-warm:#c9813f;
  --food-green:#7fa24a;
  --food-cream:#e8d2a6;
}
*{box-sizing:border-box;margin:0;padding:0}
html,body{width:1200px;height:869px;overflow:hidden}
body{background:var(--stage);position:relative;font-family:'Oswald',sans-serif;color:var(--ink)}

.card{position:absolute;left:320px;width:578px;overflow:hidden}
.card-front{top:30px;height:394px;background:var(--red);border:4px solid var(--white)}
.card-back{top:450px;height:392px;background:var(--white)}

/* front */
.photo-grid{position:absolute;left:26px;top:14px;width:390px;height:358px;display:grid;grid-template-columns:repeat(3,1fr);grid-template-rows:repeat(3,1fr);gap:6px}
.food-photo{border:3px solid var(--white);border-radius:4px}
.tone-a{background:linear-gradient(135deg,var(--food-warm),#8b3a1c)}
.tone-b{background:linear-gradient(135deg,var(--food-cream),#d14a2a)}
.tone-c{background:linear-gradient(135deg,var(--food-green),var(--food-cream))}
.tone-d{background:linear-gradient(135deg,#a8322a,var(--food-warm))}
.tone-e{background:linear-gradient(135deg,var(--food-cream),var(--food-green))}

.front-brand{position:absolute;left:420px;top:0;width:150px;height:386px}
.front-brand .rotated{position:absolute;left:50%;top:50%;width:370px;transform:translate(-50%,-50%) rotate(90deg);text-align:center}
.brand-name{font-family:'Anton',sans-serif;color:var(--white);font-size:46px;line-height:1;letter-spacing:1px}
.brand-sub{font-family:'Oswald',sans-serif;color:var(--white);font-size:20px;font-weight:400;text-align:right;margin-top:2px}
.brand-tag{font-family:'Oswald',sans-serif;color:var(--white);font-size:17px;font-weight:600;margin-top:10px}

/* back */
.coupons{position:absolute;left:8px;top:8px;width:222px;height:376px;display:flex;flex-direction:column;gap:5px}
.coupon{flex:1;border:2px dashed var(--red);padding:4px 8px;display:flex;flex-direction:column;justify-content:center;position:relative}
.coupon.light{background:var(--white);color:var(--red)}
.coupon.bold{background:var(--red);color:var(--white);border-color:var(--white);outline:2px solid var(--red)}
.coupon-head{font-family:'Anton',sans-serif;font-size:27px;line-height:1;letter-spacing:.5px}
.coupon-head small{font-size:15px;font-family:'Oswald',sans-serif;font-weight:700}
.coupon.bold .coupon-head{color:var(--yellow)}
.coupon-detail{font-size:9.5px;font-weight:600;line-height:1.2;text-transform:uppercase;margin-top:2px}
.coupon.light .coupon-detail{color:var(--ink)}
.starburst{position:absolute;right:6px;top:4px;width:22px;height:22px}

.back-info{position:absolute;left:244px;top:10px;width:326px;text-align:left}
.back-info .brand-name{color:var(--red);font-size:40px;text-align:center}
.back-info .brand-sub{color:var(--red);font-size:17px}
.back-info .brand-tag{color:var(--ink);font-size:15px;margin-top:6px;border-bottom:2px solid var(--red);padding-bottom:4px}
.find-us{margin-top:70px;text-align:center}
.find-label{color:var(--red);font-weight:700;font-size:12px}
.address{font-size:12px;font-weight:600}
.between{font-size:8px;font-weight:600;color:#555}
.phone{font-size:17px;font-weight:600;margin-top:4px;display:flex;align-items:center;justify-content:center;gap:6px}
.phone svg{width:14px;height:14px}

.thumb-row{position:absolute;left:244px;bottom:10px;width:326px;height:70px;display:grid;grid-template-columns:repeat(4,1fr);gap:6px}
.thumb-row .food-photo{border:2px solid var(--red);border-radius:3px}
</style>
</head>
<body>

<section class="card card-front">
  <div class="photo-grid">
    <div class="food-photo tone-a" role="img" aria-label="Burger and fries"></div>
    <div class="food-photo tone-b" role="img" aria-label="Pizza slice close-up"></div>
    <div class="food-photo tone-c" role="img" aria-label="Grilled chicken plate"></div>
    <div class="food-photo tone-d" role="img" aria-label="Spaghetti with meatballs"></div>
    <div class="food-photo tone-b" role="img" aria-label="Whole pepperoni pizza"></div>
    <div class="food-photo tone-a" role="img" aria-label="Calzone"></div>
    <div class="food-photo tone-e" role="img" aria-label="Wrap sandwich"></div>
    <div class="food-photo tone-c" role="img" aria-label="Greek salad"></div>
    <div class="food-photo tone-d" role="img" aria-label="Pasta sautee"></div>
  </div>
  <div class="front-brand">
    <div class="rotated">
      <div class="brand-name">MARLOW'S TRATTORIA</div>
      <div class="brand-sub">&amp; Family Restaurant</div>
      <div class="brand-tag">EAT IN or CARRY OUT and CATERING AVAILABLE</div>
    </div>
  </div>
</section>

<section class="card card-back">
  <div class="coupons">
    <div class="coupon light">
      <div class="coupon-head"><small>$</small>5.00 OFF</div>
      <div class="coupon-detail" style="font-size:13px">Any purchase of $25+</div>
      <svg class="starburst" viewBox="0 0 24 24"><polygon fill="var(--yellow)" points="12,0 15,8 24,8 17,13 20,22 12,17 4,22 7,13 0,8 9,8"/></svg>
    </div>
    <div class="coupon bold">
      <div class="coupon-head">HALF PRICE</div>
      <div class="coupon-detail">Buy 1 lunch entree, receive 2nd lunch of equal or lesser value for half price with purchase of 2 soft drinks</div>
    </div>
    <div class="coupon light">
      <div class="coupon-head"><small>$</small>5.00 OFF <small style="color:var(--ink)">2 LARGE 16"</small></div>
      <div class="coupon-detail">Pizzas with 1 or more toppings</div>
    </div>
    <div class="coupon bold">
      <div class="coupon-head">$8.99 SPECIAL</div>
      <div class="coupon-detail">Monday &amp; Tuesday: one large 16" pizza with one topping. Dine in or carry out.</div>
    </div>
    <div class="coupon light">
      <div class="coupon-head">$5.95 MEAL DEAL</div>
      <div class="coupon-detail">2 pizza slice and soda</div>
    </div>
  </div>

  <div class="back-info">
    <div class="brand-name">MARLOW'S TRATTORIA</div>
    <div class="brand-sub">&amp; Family Restaurant</div>
    <div class="brand-tag">EAT IN or CARRY OUT and CATERING AVAILABLE</div>
    <div class="find-us">
      <div class="find-label">WHERE TO FIND US</div>
      <div class="address">5172 BRASWELL POND AVE · SPRINGFIELD, VA 22987</div>
      <div class="between">(LOCATED BETWEEN BREWNOOK AND FRESH ORCHARD)</div>
      <div class="phone">
        <svg viewBox="0 0 24 24"><path fill="var(--red)" d="M6.6 10.8a15 15 0 0 0 6.6 6.6l2.2-2.2c.3-.3.7-.4 1-.2 1.1.4 2.3.6 3.6.6.6 0 1 .4 1 1V20c0 .6-.4 1-1 1A17 17 0 0 1 3 4c0-.6.4-1 1-1h3.5c.6 0 1 .4 1 1 0 1.3.2 2.5.6 3.6.1.3 0 .7-.2 1z"/></svg>
        PHONE 703-555-0148
      </div>
    </div>
  </div>

  <div class="thumb-row">
    <div class="food-photo tone-e" role="img" aria-label="Fresh sandwich"></div>
    <div class="food-photo tone-d" role="img" aria-label="Meatball pasta"></div>
    <div class="food-photo tone-c" role="img" aria-label="Side salad"></div>
    <div class="food-photo tone-b" role="img" aria-label="Cheese pizza"></div>
  </div>
</section>

</body>
</html>
```